BRIMLOW Pizza and Wraps

We need a website for a new restaurant called BRIMLOW "PIZZA AND WRAPS".
I have attached fonts, background images, logo, images, content etc.
can provide you with what you need to get the website design done fast and easy

I have uploaded more images of the venue and some menu items. let me know if there is anything I need to provide to make your mission clear and easy

Reason: i would like a little time to provide more feedback to designers

Industry/Entity Type

Restaurant

Coding

Coded - Design and coding required

Number of Pages Required

5+ page

Colors

Designer to choose colors to be used in the design.

Requirements
Must have
• PAGES:
• Our Story
• Menu
• Reservations
• Catering & Delivery
• Contact

```html
<!DOCTYPE html>
<html lang="en">
<head>
<meta charset="utf-8">
<title>Brimlow Pizza and Wraps</title>
<link rel="stylesheet" href="https://fonts.googleapis.com/css2?family=Michroma&family=Open+Sans:wght@400;600;700&display=swap">
<style>
:root{
  --red:#e3262b;
  --red-dark:#c11a1f;
  --yellow:#ffe01a;
  --ink:#1e1e1e;
  --text:#555;
  --light:#eeeeee;
  --dark:#262626;
  --white:#fff;
  --display:"Michroma",sans-serif;
  --body:"Open Sans",sans-serif;
}
*{box-sizing:border-box;margin:0;padding:0}
html,body{width:1200px;height:5014px;overflow:hidden}
body{position:relative;font-family:var(--body);color:var(--text);background:var(--light)}
section,header,footer{position:absolute;left:0;width:1200px}
.display{font-family:var(--display);text-transform:uppercase;letter-spacing:3px}
.title{font-family:var(--display);text-transform:uppercase;letter-spacing:4px;font-size:26px;color:var(--ink);text-align:center;font-weight:400}
.subtitle{font-family:var(--display);text-transform:uppercase;letter-spacing:2px;font-size:14px;color:var(--red);text-align:center}
.lead{font-size:13px;line-height:21px;text-align:center;color:var(--text)}
.btn{display:inline-block;border-radius:30px;font-family:var(--display);text-transform:uppercase;font-size:12px;letter-spacing:1px;padding:12px 28px;text-align:center;white-space:nowrap}
.btn-yellow{background:var(--yellow);color:var(--ink)}
.btn-red{background:var(--red);color:var(--white)}
.btn-outline{border:1px solid var(--red);color:var(--red)}
.round-nav{position:absolute;width:30px;height:30px;border-radius:50%;background:var(--red)}
.round-nav svg{position:absolute;left:8px;top:8px}

/* hero */
.hero{top:0;height:568px;background:linear-gradient(120deg,#3a2f2a,#6a5546 40%,#8a6c4e 60%,#2e2520)}
.hero-shade{position:absolute;inset:0;background:rgba(0,0,0,.35)}
.logo{font-family:var(--display);color:var(--red);font-size:30px;letter-spacing:2px}
.site-header{top:22px;height:60px}
.site-header .logo{position:absolute;left:182px;top:10px;font-size:26px}
.main-nav{position:absolute;left:398px;top:20px;display:flex;gap:13px;font-size:11px;font-weight:700;color:var(--white);text-transform:uppercase;white-space:nowrap}
.main-nav span{border-right:1px solid rgba(255,255,255,.4);padding-right:13px}
.main-nav span:last-child{border:none;padding-right:0}
.header-tools{position:absolute;left:958px;top:18px;display:flex;gap:10px;color:#fff;font-size:11px}
.site-header .btn{position:absolute;left:1038px;top:8px;padding:10px 18px;font-size:11px}
.hero-copy{position:absolute;left:0;top:210px;width:1200px;text-align:center;color:#fff}
.ribbon-dark{display:inline-block;background:#2a2a2a;padding:10px 60px;font-size:34px}
.ribbon-red{display:block;margin:8px auto 0;width:380px;background:var(--red);padding:8px 0;font-size:17px}
.amp{font-family:var(--display);font-size:48px;margin-top:12px}
.hero-copy .small{font-size:17px;margin-top:6px}
.hero-arrow{position:absolute;top:270px}
.dots{position:absolute;top:530px;left:0;width:1200px;display:flex;justify-content:center;gap:8px}
.dots i{width:6px;height:6px;border-radius:50%;background:rgba(255,255,255,.6)}
.dots i:first-child{background:#fff}

/* welcome */
.welcome{top:568px;height:692px;background:var(--light)}
.dish{position:absolute;top:300px;width:210px;text-align:center}
.dish .photo{width:210px;height:210px;border-radius:50%;border:6px solid #fff;box-shadow:0 2px 8px rgba(0,0,0,.2)}
.dish p{margin-top:24px;font-family:var(--display);font-size:15px;letter-spacing:3px;color:var(--ink);text-transform:uppercase}

/* story */
.story{top:1260px;height:495px;background:linear-gradient(100deg,#2c241c,#5a4530 50%,#7a5a2e 80%,#3a2c1e)}
.story .shade{position:absolute;inset:0;background:rgba(0,0,0,.45)}
.story .title{color:#fff;position:absolute;top:150px;width:100%}
.story .lead{color:#eee;position:absolute;left:260px;top:218px;width:680px}

/* menu */
.menu{top:1755px;height:836px;background:#f3f3f3}
.tabs{position:absolute;top:290px;left:165px;width:870px;display:flex;justify-content:space-around;font-family:var(--display);font-size:13px;letter-spacing:2px;color:var(--ink);text-transform:uppercase}
.tab-line{position:absolute;top:322px;left:165px;width:160px;height:2px;background:var(--red)}
.tab-base{position:absolute;top:323px;left:165px;width:870px;height:1px;background:#ddd}
.tab-icon{position:absolute;top:380px;width:100px;height:100px;border-radius:50%;border:4px solid #fff;box-shadow:0 1px 6px rgba(0,0,0,.2)}
.item{position:absolute;width:400px;border-bottom:1px solid #ccc;padding-bottom:8px}
.item h4{font-size:15px;font-weight:700;color:var(--ink);display:flex;justify-content:space-between}
.item h4 b{color:var(--red)}
.item .tag{font-size:9px;background:var(--yellow);padding:2px 8px;margin-left:70px;font-weight:600}
.item-desc{position:absolute;font-size:11px;color:#888}

/* bands */
.band{background:linear-gradient(90deg,var(--red-dark),var(--red) 40%,var(--red) 70%,var(--red-dark))}
.band h2{font-family:var(--display);text-transform:uppercase;color:#fff;font-size:22px;line-height:46px;letter-spacing:3px;font-weight:400}
.delivery{top:2591px;height:251px}
.delivery h2{position:absolute;left:178px;top:34px;width:900px}
.delivery .icon{position:absolute;left:178px;top:160px;width:48px;height:48px;border-radius:50%;background:#fff}
.delivery p{position:absolute;left:242px;top:174px;color:#fff;font-size:14px}
.delivery .btn{position:absolute;left:795px;top:164px}

/* news */
.news{top:2842px;height:678px;background:#f3f3f3}
.card{position:absolute;top:218px;width:270px}
.card .date{font-size:10px;color:var(--red)}
.card h3{font-size:17px;font-weight:600;color:var(--ink);margin-top:6px;text-transform:uppercase}
.card .photo{height:195px;margin-top:12px}
.card p{font-size:10px;line-height:16px;color:#777;margin-top:14px}
.card .more{font-size:11px;color:var(--ink);margin-top:16px}

.events{top:3520px;height:291px}
.events h2{position:absolute;left:178px;top:30px;width:880px;line-height:44px}
.events p{position:absolute;left:180px;top:190px;width:420px;color:#fff;font-size:14px;line-height:20px}
.events .btn{position:absolute;left:735px;top:188px}

.map{top:3811px;height:351px;background:linear-gradient(120deg,#d9dfd2,#c8d4bd 50%,#b8caa8)}
.map svg{position:absolute;left:453px;top:80px}

/* hours */
.hours{top:4162px;height:501px;background:linear-gradient(90deg,#c0472a,#d68a36 25%,#6b3a22 45%,#a0522d 70%,#7a3b1e)}
.hours-box{position:absolute;left:180px;top:82px;width:320px;height:370px;background:rgba(255,224,26,.92);text-align:center;padding-top:40px;color:var(--ink)}
.hours-box h3{font-family:var(--display);font-size:20px;letter-spacing:3px;font-weight:400;color:var(--red);text-transform:uppercase}
.hours-box p{font-size:14px;line-height:22px;margin-top:18px}
.hours-box .btn{margin-top:28px;border:2px solid var(--red);color:var(--red);padding:9px 20px;font-size:11px}

/* footer */
.site-footer{top:4663px;height:351px;background:var(--dark);text-align:center}
.site-footer .logo{position:absolute;top:72px;width:100%;font-size:40px}
.foot-nav{position:absolute;top:176px;width:100%;display:flex;justify-content:center;gap:40px;color:#ddd;font-size:13px}
.social{position:absolute;top:218px;width:100%;display:flex;justify-content:center;gap:12px}
.social i{width:26px;height:26px;border-radius:50%;background:var(--red)}
.foot-rule{position:absolute;top:270px;left:180px;width:840px;height:1px;background:#3c3c3c}
.copyright{position:absolute;top:292px;width:100%;font-size:11px;color:#aaa}
.to-top{position:absolute;left:1110px;top:262px;width:34px;height:34px;border-radius:50%;background:var(--yellow)}
.to-top svg{position:absolute;left:10px;top:10px}
</style>
</head>
<body>

<section class="hero" role="img" aria-label="Photo of pizzas and dishes on a restaurant table">
  <div class="hero-shade"></div>
  <header class="site-header">
    <div class="logo">BRIMLOW</div>
    <nav class="main-nav"><span>Home</span><span>Our Story</span><span>Menu</span><span>Reservations</span><span>Catering &amp; Delivery</span><span>Contact</span></nav>
    <div class="header-tools">
      <svg width="16" height="14" viewBox="0 0 16 14" fill="none" stroke="#fff" stroke-width="1.5"><path d="M1 1h3l2 8h8l1.5-6H5"/><circle cx="7" cy="12" r="1"/><circle cx="13" cy="12" r="1"/></svg><span>0</span>
      <svg width="13" height="13" viewBox="0 0 13 13" fill="none" stroke="#fff" stroke-width="1.5"><circle cx="5.5" cy="5.5" r="4"/><path d="M8.5 8.5L12 12"/></svg>
    </div>
    <span class="btn btn-yellow">Book a Table</span>
  </header>
  <svg class="hero-arrow" style="left:34px" width="16" height="30" viewBox="0 0 16 30" fill="none" stroke="#fff" stroke-width="2"><path d="M14 2L2 15l12 13"/></svg>
  <svg class="hero-arrow" style="left:1150px" width="16" height="30" viewBox="0 0 16 30" fill="none" stroke="#fff" stroke-width="2"><path d="M2 2l12 13L2 28"/></svg>
  <div class="hero-copy">
    <div class="ribbon-dark display">Discover</div>
    <div class="ribbon-red display">Mediterranean Tastes</div>
    <div class="amp">&amp;</div>
    <div class="display small">Crafted Beverages</div>
  </div>
  <div class="dots"><i></i><i></i><i></i><i></i></div>
</section>

<section class="welcome">
  <h2 class="title" style="position:absolute;top:50px;width:100%">Welcome to Brimlow</h2>
  <p class="subtitle" style="position:absolute;top:104px;width:100%">Perfect spot to enjoy sensational food and drinks</p>
  <p class="lead" style="position:absolute;top:140px;left:350px;width:500px">We combined a variety of best ingredients and delicacies for you to enjoy that experience whenever you get the urge to do so.</p>
  <div class="dish" style="left:195px"><div class="photo" role="img" aria-label="Bowl of hummus" style="background:radial-gradient(#e8c25a,#c9943a 60%,#f2e0b0)"></div><p>BM Hummus</p></div>
  <div class="dish" style="left:497px"><div class="photo" role="img" aria-label="Pizza slices" style="background:radial-gradient(#d86a3a,#a84320 60%,#e2b27a)"></div><p>BM Pizza</p></div>
  <div class="dish" style="left:791px"><div class="photo" role="img" aria-label="Wraps on a plate" style="background:radial-gradient(#d9c39a,#a88a5a 60%,#6a5236)"></div><p>BM Wrap</p></div>
  <span class="round-nav" style="left:565px;top:617px"><svg width="14" height="14" viewBox="0 0 14 14" fill="none" stroke="#fff" stroke-width="2"><path d="M9 2L4 7l5 5"/></svg></span>
  <span class="round-nav" style="left:605px;top:617px"><svg width="14" height="14" viewBox="0 0 14 14" fill="none" stroke="#fff" stroke-width="2"><path d="M5 2l5 5-5 5"/></svg></span>
</section>

<section class="story" role="img" aria-label="Photo of the restaurant interior with brick walls and warm lighting">
  <div class="shade"></div>
  <h2 class="title">Our Story</h2>
  <p class="lead">Born in heritage, Brimlow is a gathering place celebrating the Mediterranean's finest Produce. Brimlow is the ultimate escape – the perfect spot to enjoy sensational food and drinks that showcases everything the Mediterranean has to offer in a simple, sophisticated setting.</p>
  <span class="btn btn-red" style="position:absolute;left:518px;top:340px">Read More</span>
</section>

<section class="menu">
  <h2 class="title" style="position:absolute;top:52px;width:100%">Our Enchanting Menu</h2>
  <p class="subtitle" style="position:absolute;top:100px;width:100%">Deliciousness, this is where it happens</p>
  <p class="lead" style="position:absolute;top:138px;left:300px;width:600px">Quality food is devotion to seasonal, fresh ingredients, and meticulous care in bringing it to life on the plate. At Brimlow, the emphasis is on an experience that extends those great items to a relaxed, warm environment of the venue.</p>
  <div class="tabs"><span>Pizza</span><span>Wrap</span><span>Halloumi</span><span>Hummus</span></div>
  <div class="tab-base"></div><div class="tab-line"></div>
  <div class="tab-icon" role="img" aria-label="Pizza" style="left:193px;background:radial-gradient(#e07a3a,#b04a22)"></div>
  <div class="tab-icon" role="img" aria-label="Wrap" style="left:420px;background:radial-gradient(#c8a06a,#6a4a30)"></div>
  <div class="tab-icon" role="img" aria-label="Halloumi" style="left:665px;background:radial-gradient(#e6d39a,#9aa850)"></div>
  <div class="tab-icon" role="img" aria-label="Hummus" style="left:893px;background:radial-gradient(#e8c25a,#c9943a)"></div>
  <div class="item" style="left:170px;top:528px"><h4>MARGHERITA <b>$ 25</b></h4></div>
  <p class="item-desc" style="left:170px;top:572px">Tomatoes, mozzarella, basil</p>
  <div class="item" style="left:628px;top:528px"><h4>POMODORI <b>$ 20</b></h4></div>
  <p class="item-desc" style="left:628px;top:572px">Tomatoes, capers, olives</p>
  <div class="item" style="left:170px;top:618px"><h4><span>PACHINO<span class="tag">NEW</span></span> <b>$ 18</b></h4></div>
  <p class="item-desc" style="left:170px;top:662px">Cherry tomatoes, rocket, cheese</p>
  <div class="item" style="left:628px;top:618px"><h4>SALMONE PESTO DI <b>$ 28</b></h4></div>
  <p class="item-desc" style="left:628px;top:662px">Salmon, pesto, onion</p>
  <span class="btn btn-outline" style="position:absolute;left:515px;top:752px;padding:10px 22px;font-size:11px">Explore Full Menu</span>
</section>

<section class="delivery band">
  <h2>Brimlow delivers directly where you<br>want it within our coverage area</h2>
  <div class="icon"></div>
  <p>This service is available during restaurant hours</p>
  <span class="btn btn-yellow">Make an Order Now</span>
</section>

<section class="news">
  <h2 class="title" style="position:absolute;top:62px;width:100%">News &amp; Events</h2>
  <p class="subtitle" style="position:absolute;top:112px;width:100%">A special event requires a unique experience</p>
  <div class="card" style="left:172px">
    <p class="date">September 29, 2017</p><h3>Velit esse quam nihil</h3>
    <div class="photo" role="img" aria-label="Restaurant entrance with red awning" style="background:linear-gradient(90deg,#7a3020,#b8452a,#4a3a30)"></div>
    <p>Fresh dough, slow sauce and long tables: our new season starts with a weekend of tastings, live music and open kitchen tours for every guest.</p>
    <p class="more">read more →</p>
  </div>
  <div class="card" style="left:462px">
    <p class="date">September 22, 2017</p><h3>Reiciendis</h3>
    <div class="photo" role="img" aria-label="Dining room set for an evening event" style="background:linear-gradient(90deg,#3a2a22,#a8743a,#5a3a28)"></div>
    <p>Book the dining room for your birthday, team dinner or family party and let our chefs plan a shared Mediterranean menu just for you.</p>
    <p class="more">read more →</p>
  </div>
  <div class="card" style="left:755px">
    <p class="date">September 15, 2017</p><h3>Quam nihil molestiae</h3>
    <div class="photo" role="img" aria-label="Plate of fresh salad" style="background:linear-gradient(90deg,#6a8a3a,#c86a4a,#e8d8b0)"></div>
    <p>Our halloumi salad returns with grilled peppers, mint and lemon, served daily with warm bread straight from the oven.</p>
    <p class="more">read more →</p>
  </div>
  <span class="round-nav" style="left:565px;top:620px"><svg width="14" height="14" viewBox="0 0 14 14" fill="none" stroke="#fff" stroke-width="2"><path d="M9 2L4 7l5 5"/></svg></span>
  <span class="round-nav" style="left:605px;top:620px"><svg width="14" height="14" viewBox="0 0 14 14" fill="none" stroke="#fff" stroke-width="2"><path d="M5 2l5 5-5 5"/></svg></span>
</section>

<section class="events band">
  <h2>Do you have to organize lunches or<br>dinners, business events or private<br>parties?</h2>
  <p>Brimlow will recreate a Mediterranean atmosphere in your home or wherever you prefer</p>
  <span class="btn btn-yellow">Send Your Request</span>
</section>

<section class="map" role="img" aria-label="Map showing the restaurant location">
  <svg width="26" height="36" viewBox="0 0 26 36"><path d="M13 0C6 0 0 6 0 13c0 9 13 23 13 23s13-14 13-23C26 6 20 0 13 0z" fill="#e3262b"/><circle cx="13" cy="13" r="5" fill="#fff"/></svg>
</section>

<section class="hours" role="img" aria-label="Photo of the restaurant dining room with a wooden door and brick wall">
  <div class="hours-box">
    <h3>Opening Hours</h3>
    <p>Daily from: 8am – 11pm<br>Friday: Closed from 1am – 2pm</p>
    <p>Call +1 555 014 2290<br>or fill out the reservation form</p>
    <span class="btn">Make a Reservation</span>
  </div>
</section>

<footer class="site-footer">
  <div class="logo">BRIMLOW</div>
  <nav class="foot-nav"><span>Home</span><span>Our Story</span><span>Menu</span><span>Reservation</span><span>Catering &amp; Delivery</span><span>Contact</span></nav>
  <div class="social"><i></i><i></i></div>
  <div class="foot-rule"></div>
  <p class="copyright">© Copyright Brimlow Pizza and Wraps. All rights reserved.</p>
  <span class="to-top"><svg width="14" height="14" viewBox="0 0 14 14" fill="none" stroke="#262626" stroke-width="2"><path d="M2 9l5-5 5 5"/></svg></span>
</footer>

</body>
</html>
```